Zelvrin
business cards & stationery
Project: Zelvrin
Zelvrin -
Creative Brief
Simple
Marcus Holt
VP Sales & Marketing
417 Fenwick Ave. #615-284 Brookmere Falls, NV 89733
temporary@zelvrin-example.com
www.zelvrin-example.com
Your Game, Everywhere

```html
<!DOCTYPE html>
<html lang="en">
<head>
<meta charset="utf-8">
<title>Zelvrin Stationery</title>
<link href="https://fonts.googleapis.com/css2?family=Open+Sans:wght@400;600;700&display=swap" rel="stylesheet">
<style>
  :root{
    --stage:#0d2a63;
    --paper:#ffffff;
    --ink:#4a4f57;
    --ink-soft:#7b8089;
    --brand:#1f6fd1;
    --brand-deep:#0b3c9a;
    --brand-light:#5fa8f0;
  }
  *{box-sizing:border-box;margin:0;padding:0}
  html,body{width:1200px;height:737px;overflow:hidden}
  body{background:var(--stage);font-family:"Open Sans",Arial,sans-serif;color:var(--ink);position:relative}
  .sheet{position:absolute;background:var(--paper)}
  .wordmark{display:flex;align-items:center;gap:6px;font-weight:700;color:var(--ink);letter-spacing:.5px}
  .wordmark .dot{display:inline-block;border-radius:50%;background:var(--brand)}
  .address{font-size:8px;line-height:1.45;color:var(--ink-soft)}

  /* Envelope #10 */
  .envelope{left:24px;top:276px;width:420px;height:182px}
  .envelope .wordmark{position:absolute;left:22px;top:22px;font-size:22px}
  .envelope .wordmark .dot{width:10px;height:10px}
  .envelope .address{position:absolute;left:22px;top:56px;font-size:6.5px}

  /* Letterhead */
  .letterhead{left:462px;top:48px;width:300px;height:388px}
  .letterhead .wordmark{position:absolute;left:26px;top:34px;font-size:22px}
  .letterhead .wordmark .dot{width:10px;height:10px}
  .letterhead .contact{position:absolute;left:172px;top:22px;font-size:6px;line-height:1.6;color:var(--ink-soft)}
  .contact-row{display:flex;align-items:center;gap:5px}
  .contact-row svg{flex:none}
  .contact .spacer{height:4px}

  /* Business card front */
  .card-front{left:782px;top:48px;width:360px;height:206px}
  .card-front .wordmark{position:absolute;left:18px;top:24px;font-size:26px}
  .card-front .wordmark .dot{width:12px;height:12px}
  .card-front .address{position:absolute;left:200px;top:14px;font-size:6.5px}
  .card-front .contact{position:absolute;left:200px;top:72px;font-size:7px;line-height:1.75;color:var(--ink-soft)}
  .card-front .nameplate{position:absolute;left:0;bottom:26px;width:190px;padding:6px 18px;border-top:1px solid #dfe6ef;border-bottom:1px solid #dfe6ef;display:flex;align-items:baseline;gap:8px}
  .nameplate .name{font-size:11px;font-weight:700;color:var(--brand);text-transform:uppercase;letter-spacing:.5px}
  .nameplate .title{font-size:6.5px;color:var(--ink-soft)}

  /* Business card back */
  .card-back{left:782px;top:272px;width:360px;height:206px;background:radial-gradient(circle at 50% 50%,var(--brand-light) 0%,var(--brand) 45%,var(--brand-deep) 100%)}
</style>
</head>
<body>

<section class="sheet envelope" aria-label="Envelope #10">
  <div class="wordmark"><span>Zelvrin</span><span class="dot"></span></div>
  <p class="address">417 Fenwick Ave. #615-284<br>Brookmere Falls, NV 89733</p>
</section>

<section class="sheet letterhead" aria-label="Letterhead">
  <div class="wordmark"><span>Zelvrin</span><span class="dot"></span></div>
  <div class="contact">
    <p>417 Fenwick Ave. #615-284<br>Brookmere Falls, NV 89733</p>
    <div class="spacer"></div>
    <p class="contact-row"><svg width="6" height="6" viewBox="0 0 10 10"><path d="M2 1h2l1 2-1.5 1a6 6 0 0 0 2.5 2.5L7 5l2 1v2a1 1 0 0 1-1 1A8 8 0 0 1 1 2a1 1 0 0 1 1-1z" fill="#7b8089"/></svg>(111) 111-1111</p>
    <p class="contact-row"><svg width="6" height="6" viewBox="0 0 10 10"><rect x="2.5" y="0.5" width="5" height="9" rx="1" fill="#7b8089"/></svg>(111) 111-1111</p>
    <p class="contact-row"><svg width="6" height="6" viewBox="0 0 10 10"><rect x="1" y="3" width="8" height="5" fill="#7b8089"/><rect x="3" y="1" width="4" height="2" fill="#7b8089"/></svg>(111) 111-1111</p>
    <p class="contact-row"><svg width="6" height="6" viewBox="0 0 10 10"><rect x="0.5" y="2" width="9" height="6" fill="none" stroke="#7b8089"/><path d="M1 2.5l4 3 4-3" fill="none" stroke="#7b8089"/></svg>temporary@zelvrin-example.com</p>
    <p class="contact-row"><svg width="6" height="6" viewBox="0 0 10 10"><circle cx="5" cy="5" r="4.5" fill="#7b8089"/></svg><strong>www.zelvrin-example.com</strong></p>
  </div>
</section>

<section class="sheet card-front" aria-label="Business card front">
  <div class="wordmark"><span>Zelvrin</span><span class="dot"></span></div>
  <p class="address">417 Fenwick Ave. #615-284<br>Brookmere Falls, NV 89733</p>
  <div class="contact">
    <p class="contact-row"><svg width="7" height="7" viewBox="0 0 10 10"><path d="M2 1h2l1 2-1.5 1a6 6 0 0 0 2.5 2.5L7 5l2 1v2a1 1 0 0 1-1 1A8 8 0 0 1 1 2a1 1 0 0 1 1-1z" fill="#7b8089"/></svg>(111) 111-1111</p>
    <p class="contact-row"><svg width="7" height="7" viewBox="0 0 10 10"><rect x="2.5" y="0.5" width="5" height="9" rx="1" fill="#7b8089"/></svg>(111) 111-1111</p>
    <p class="contact-row"><svg width="7" height="7" viewBox="0 0 10 10"><rect x="1" y="3" width="8" height="5" fill="#7b8089"/><rect x="3" y="1" width="4" height="2" fill="#7b8089"/></svg>(111) 111-1111</p>
    <p class="contact-row"><svg width="7" height="7" viewBox="0 0 10 10"><rect x="0.5" y="2" width="9" height="6" fill="none" stroke="#7b8089"/><path d="M1 2.5l4 3 4-3" fill="none" stroke="#7b8089"/></svg>temporary@zelvrin-example.com</p>
    <p class="contact-row"><svg width="7" height="7" viewBox="0 0 10 10"><circle cx="5" cy="5" r="4.5" fill="#7b8089"/></svg><strong>www.zelvrin-example.com</strong></p>
  </div>
  <div class="nameplate">
    <span class="name">Marcus Holt</span>
    <span class="title">VP Sales &amp; Marketing</span>
  </div>
</section>

<section class="sheet card-back" role="img" aria-label="Business card back: blue radial field with glowing bubble artwork"></section>

</body>
</html>
```